Upmarket cover for top management book, ideally unlike most common cover pages

This book is about both good management and mismanagement and introduces novel concepts such as the inverse exponential law in strategy, No doubt that these concepts will be criticized by some management scholars. However, students, a few other colleagues and key top managers find the new ideas useful and eye-opening.
The cover must help communicate a deeper vision of management as an expression of life creation and a sort of "divine" energy.

Practical details:
Print and ebook cover page plus elements of the cover for each of the three main book sections.
Title; The Harbor
Subtitle: Field methods and the quiet ripple rule
Author: Teodor M. Vasquel
Publisher: Brightwell Page Press
Width x height: 13,97 x 21,59 cm (without bleed)
Spine: 14-15 cm according to paper color

Target Market(s)

Mostly managers who did not have the opportunity of attending postgraduate management studies such as the MBA

Industry/Entity Type

Mostly high technology

Font styles to use
Serif
Sans Serif
Other font styles liked:
• Arial nova, Arial light

Requirements
Must have
• Preferably cover and back cover on white background, but any good proposals would do.
Nice to have
• An image of bright and reassuring, albeit potentially unlimited, strength. Ideally the cover design should show that good management is good for the COMMON GOOD of society
Should not have
• Please do not show images of people and no proposals reminiscent of other management and strategy book covers

```html
<!DOCTYPE html>
<html lang="en">
<head>
<meta charset="utf-8">
<title>The Harbor — Teodor M. Vasquel</title>
<link rel="stylesheet" href="https://fonts.googleapis.com/css2?family=Cormorant+Garamond:wght@500;600&family=Pinyon+Script&family=Montserrat:wght@600&display=swap">
<style>
  :root {
    --gold: #ecdca4;
    --gold-deep: #b99a55;
    --violet: #5a1f6e;
    --indigo: #241a55;
    --ember: #e2412a;
    --flame: #f7823a;
    --magenta: #c24fb0;
    --teal: #2fb3b0;
    --night: #0f1330;
  }
  * { margin: 0; padding: 0; box-sizing: border-box; }
  html, body { width: 861px; height: 1200px; overflow: hidden; background: var(--night); }
  .cover {
    position: relative;
    width: 861px;
    height: 1200px;
    overflow: hidden;
  }
  .cosmic-artwork {
    position: absolute;
    inset: 0;
    background:
      radial-gradient(circle at 82% 14%, rgba(255,215,150,0.85) 0, var(--flame) 8%, rgba(226,65,42,0.9) 22%, rgba(226,65,42,0) 48%),
      radial-gradient(ellipse at 52% 62%, rgba(255,190,220,0.75) 0, rgba(194,79,176,0.55) 20%, rgba(194,79,176,0) 45%),
      radial-gradient(ellipse at 55% 88%, rgba(47,179,176,0.55) 0, rgba(47,179,176,0) 40%),
      radial-gradient(ellipse at 20% 40%, rgba(90,31,110,0.9) 0, rgba(90,31,110,0) 55%),
      linear-gradient(180deg, var(--violet) 0%, #6b2a7a 35%, #3d3a8c 62%, var(--indigo) 82%, var(--night) 100%);
  }
  .headline {
    position: absolute;
    inset: 0;
    width: 861px;
    height: 1200px;
  }
  .title-lead {
    font-family: "Pinyon Script", cursive;
    font-size: 170px;
    fill: var(--gold);
  }
  .title-main, .author {
    font-family: "Cormorant Garamond", serif;
    font-weight: 600;
    fill: var(--gold);
    filter: drop-shadow(2px 3px 3px rgba(40,10,30,0.55));
  }
  .title-main { font-size: 250px; }
  .author { font-size: 118px; }
  .subtitle {
    position: absolute;
    right: 25px;
    top: 412px;
    text-align: right;
    font-family: "Montserrat", sans-serif;
    font-weight: 600;
    font-size: 29px;
    line-height: 43px;
    color: var(--gold);
    text-transform: uppercase;
    letter-spacing: 0.01em;
  }
</style>
</head>
<body>
<main class="cover">
  <div class="cosmic-artwork" role="img" aria-label="Glowing cosmic nebula in violet, red and blue with a rainbow path of light leading into the distance"></div>

  <svg class="headline" viewBox="0 0 861 1200" aria-hidden="false">
    <text class="title-lead" x="150" y="215">The</text>
    <text class="title-main" x="25" y="396" textLength="822" lengthAdjust="spacingAndGlyphs">HARBOR</text>
    <text class="author" x="58" y="1163" textLength="756" lengthAdjust="spacingAndGlyphs">TEODOR M. VASQUEL</text>
  </svg>

  <p class="subtitle">Field methods<br>and the quiet ripple rule</p>
</main>
</body>
</html>
```